Artificial intelligence, machine learning, and automation company needs a sexy business card design

We need a sleek and sexy business card design for an AI consulting company based in Philadelphia PA. We provide custom machine learning and automation solutions for companies of all shapes and sizes. The primary industries that we serve are pharmaceuticals, engineering, healthcare, and computer software. We would like the designs to be a black business card that uses green as a sleek accent color. The final design should communicate intelligence, cutting edge new-tech, and optimization.

Target Market(s)

C-level and VP level executives of multi-million annual companies. Mostly in Pharma, Healthcare, Real Estate, Retail, and Engineering

Industry/Entity Type

Computer Software

Contact Information for Business Card

Name: Jack Moss
Title: CEO
Cell: 215 604 8293
Email: JackM@quillarcworks.example
Website: www.QuillarcWorks.example

Font styles to use
Sans Serif

Colors

Designer to choose colors to be used in the design.

Requirements
Must have
• 1) Attached Quillarc Logo (either with colors or not/embossed)
• 2) "Artificial Intelligence" "Automation" and "Machine Learning"
• 3) "Quillarc Laboratories" or "Quillarc Works" or "Quillarc"
• 4) Sexy AF.
Nice to have
• Black card / dark card color, "Quillarc Green" accent colors (in attached .ai file), Embossment of logo/name/etc, thick card stock, colored borders (on card sides, not front/back faces)
Should not have
• Should not be bland, or unsexy.

```html
<!DOCTYPE html>
<html lang="en">
<head>
<meta charset="utf-8">
<title>Quillarc Works — Business Card</title>
<link rel="stylesheet" href="https://fonts.googleapis.com/css2?family=Roboto:wght@300;400;500;700&display=swap">
<style>
  :root {
    --backdrop: #8c8c8c;
    --card-white: #f3f3f3;
    --charcoal: #4b4b4b;
    --quillarc-green: #58c3b0;
    --ink: #1e1e1e;
    --white: #ffffff;
  }
  * { box-sizing: border-box; margin: 0; padding: 0; }
  html, body { width: 1200px; height: 1200px; overflow: hidden; }
  body {
    background: var(--backdrop);
    font-family: "Roboto", Arial, sans-serif;
    position: relative;
  }
  .card {
    position: absolute;
    top: 310px;
    height: 594px;
    box-shadow: 2px 3px 6px rgba(0,0,0,0.35);
    overflow: hidden;
  }
  /* Front */
  .card-front {
    left: 234px;
    width: 364px;
    background: var(--card-white);
    text-align: center;
  }
  .brand-square {
    position: absolute;
    left: 80px; top: 66px;
    width: 204px; height: 196px;
    background: var(--charcoal);
    border: 8px solid var(--quillarc-green);
  }
  .brand-name {
    position: absolute;
    left: 0; right: 0;
    color: var(--charcoal);
    font-weight: 300;
  }
  .brand-name--main { top: 270px; font-size: 40px; letter-spacing: 6px; }
  .brand-name--sub { top: 316px; font-size: 19px; letter-spacing: 4.4px; }
  .holder-name {
    position: absolute; left: 0; right: 0; top: 386px;
    color: var(--quillarc-green);
    font-weight: 500; font-size: 23px;
  }
  .holder-title {
    position: absolute; left: 0; right: 0; top: 416px;
    color: var(--ink); font-size: 17px;
  }
  .contact-divider {
    position: absolute; left: 83px; top: 456px;
    width: 198px; height: 24px;
  }
  .contact-list {
    position: absolute; left: 0; right: 0; top: 488px;
    list-style: none;
    color: var(--ink); font-size: 17px; line-height: 21.5px;
  }
  /* Back */
  .card-back {
    left: 627px;
    width: 370px;
    background: var(--quillarc-green);
  }
  .back-band {
    position: absolute; left: 0; top: 0;
    width: 100%; height: 122px;
    background: var(--charcoal);
  }
  .back-brand {
    position: absolute; left: 0; right: 0; top: 260px;
    text-align: center;
    color: var(--white);
    font-weight: 300; font-size: 44px; letter-spacing: 8px;
  }
  .services {
    position: absolute; left: 0; right: 0; top: 494px;
    list-style: none; text-align: center;
    color: var(--ink); font-size: 18px; line-height: 24.5px;
  }
</style>
</head>
<body>
  <section class="card card-front">
    <div class="brand-square"></div>
    <div class="brand-name brand-name--main">QUILLARC</div>
    <div class="brand-name brand-name--sub">LABORATORIES</div>
    <div class="holder-name">JACK MOSS</div>
    <div class="holder-title">CEO</div>
    <svg class="contact-divider" viewBox="0 0 198 24" aria-hidden="true">
      <line x1="0" y1="12" x2="56" y2="12" stroke="#1e1e1e" stroke-width="1.2"/>
      <line x1="142" y1="12" x2="198" y2="12" stroke="#1e1e1e" stroke-width="1.2"/>
      <rect x="63" y="1" width="22" height="22" fill="#4b4b4b"/>
      <rect x="88" y="1" width="22" height="22" fill="#4b4b4b"/>
      <rect x="113" y="1" width="22" height="22" fill="#4b4b4b"/>
      <path d="M69 6 l3 0 l1.5 3.5 l-1.8 1.3 q1.5 3 4 4.2 l1.3 -1.8 l3.5 1.5 l0 3 q-8 1 -11.5 -11.7z" fill="#58c3b0"/>
      <rect x="93" y="7" width="12" height="9" fill="#58c3b0"/>
      <path d="M93 7 l6 5 l6 -5" fill="none" stroke="#4b4b4b" stroke-width="1"/>
      <circle cx="124" cy="12" r="6.5" fill="#58c3b0"/>
      <path d="M117.5 12 h13 M124 5.5 q-4 6.5 0 13 M124 5.5 q4 6.5 0 13" fill="none" stroke="#4b4b4b" stroke-width="0.9"/>
    </svg>
    <ul class="contact-list">
      <li>215 604 8293</li>
      <li>JackM@quillarcworks.example</li>
      <li>www.QuillarcWorks.example</li>
    </ul>
  </section>

  <section class="card card-back">
    <div class="back-band"></div>
    <div class="back-brand">QUILLARC</div>
    <ul class="services">
      <li>Artificial Intelligence</li>
      <li>Automation</li>
      <li>Machine Learning</li>
    </ul>
  </section>
</body>
</html>
```